Poster Needed for Church Conference

I need a poster for a weekend conference at my church. Looking to attract as many people as possible. We are a church in the suburbs of Houston. This is mainly for our own church members but we are opening it up to outside church members.

Please see previous design from last conference and all other graphic work that can (doesn't need to be) included.

Target Market(s)

It's targeted for all people. But our main audience is families. around the age of 30 should be main target.

Industry/Entity Type

Non-Profit

Font styles to use
Serif
Sans Serif

Colors

Designer to choose colors to be used in the design.

Requirements
Must have
• 11x17 design with ability to shrink and blow up. but ideally for 11x17
• Content and wording:
• "Rooted Lantern Conference: Bridging the gap between generations and passing on our deepest beliefs and values."
• Featuring Dr. Glen Marlowe. Author of "The Map of Q9"
• Aug 25-26: Friday 8-10 pm, Saturday 4-8 pm
• Cost Adults $15/Children $5: Covers admission to all sessions and workshops, refreshments and Saturday dinner. *kids 5 and under free
• Childcare provided for all sessions. "
• Please use church logo and address on flyer: 4312 Orchard Bend, Missouri City, TX 77512
Nice to have
• Ideally it will be designed so that we can crop a 16:9 pp announcement slide and header for our website.
Should not have
• anything offensive

```html
<!DOCTYPE html>
<html lang="en">
<head>
<meta charset="utf-8">
<title>Rooted Lantern Conference</title>
<link rel="stylesheet" href="https://fonts.googleapis.com/css2?family=Roboto+Condensed:wght@300;400;500;700&family=Cormorant+Garamond:wght@400&family=Mr+Dafoe&display=swap">
<style>
  :root {
    --brown-dark: #2b1f17;
    --brown-mid: #4a3727;
    --green-base: #1f4d24;
    --green-accent: #2f9a3c;
    --white: #ffffff;
    --rose: #e8204f;
    --rule: rgba(255,255,255,0.35);
  }
  * { margin: 0; padding: 0; box-sizing: border-box; }
  html, body { width: 776px; height: 1200px; overflow: hidden; background: var(--green-base); }
  .poster {
    position: relative; width: 776px; height: 1200px; overflow: hidden;
    background: var(--green-base); color: var(--white);
    font-family: "Roboto Condensed", sans-serif;
  }
  .scene-photo {
    position: absolute; left: 0; top: 0; width: 776px; height: 900px;
    background:
      radial-gradient(ellipse 190px 260px at 190px 420px, rgba(196,140,110,0.55), transparent 75%),
      radial-gradient(ellipse 140px 90px at 640px 120px, rgba(120,90,60,0.35), transparent 80%),
      linear-gradient(180deg, var(--brown-dark) 0%, var(--brown-mid) 45%, #3a3020 70%, var(--green-base) 100%);
  }
  .event-title {
    position: absolute; left: 400px; width: 320px; top: 208px;
    text-align: center; font-weight: 700; font-size: 22px;
  }
  .tagline {
    position: absolute; left: 376px; width: 392px; top: 256px;
    text-align: center; font-family: "Cormorant Garamond", serif; font-weight: 400;
    font-size: 44px; line-height: 52px; letter-spacing: 0.5px; white-space: nowrap;
  }
  .speaker-name {
    position: absolute; right: 28px; top: 556px;
    font-family: "Mr Dafoe", cursive; font-weight: 400; font-size: 53px; line-height: 70px;
    color: var(--rose); white-space: nowrap;
  }
  .book-title {
    position: absolute; right: 37px; top: 643px;
    font-weight: 700; font-size: 24px; letter-spacing: 2px;
  }
  .book-badge {
    position: absolute; left: 290px; top: 773px; width: 196px; height: 73px;
    background: var(--white); display: flex; align-items: center; justify-content: center;
    color: var(--green-accent); font-weight: 700; font-size: 24px;
  }
  .event-date {
    position: absolute; left: 0; width: 776px; top: 866px; text-align: center;
    font-weight: 700; font-size: 54px;
  }
  .event-times {
    position: absolute; left: 0; width: 776px; top: 940px; text-align: center;
    font-weight: 300; font-size: 29px;
  }
  .rule { position: absolute; left: 82px; width: 612px; height: 1px; background: var(--rule); }
  .rule-top { top: 997px; }
  .rule-bottom { top: 1097px; }
  .cost-tag { position: absolute; left: 109px; top: 1015px; width: 90px; height: 65px; }
  .cost-tag span {
    position: absolute; left: 0; width: 82px; top: 17px; text-align: center;
    color: var(--green-accent); font-weight: 700; font-size: 25px;
  }
  .price { position: absolute; top: 1012px; text-align: center; }
  .price-amount { font-weight: 700; font-size: 40px; line-height: 44px; }
  .price-label { font-weight: 500; font-size: 24px; line-height: 30px; }
  .price-adult { left: 215px; width: 70px; }
  .price-child { left: 339px; width: 80px; }
  .divider { position: absolute; top: 1012px; width: 1px; height: 74px; background: var(--white); }
  .divider-a { left: 311px; }
  .divider-b { left: 442px; }
  .cost-note {
    position: absolute; left: 461px; top: 1020px; width: 230px;
    font-weight: 500; font-size: 22px; line-height: 29px;
  }
  .footnote {
    position: absolute; left: 0; width: 776px; top: 1118px; text-align: center;
    font-weight: 500; font-size: 17px; line-height: 22px;
  }
  .church-line {
    position: absolute; left: 0; width: 776px; top: 1170px;
    display: flex; align-items: center; justify-content: center; gap: 8px;
    font-weight: 500; font-size: 15px; line-height: 20px;
  }
  .church-mark { width: 10px; height: 10px; border-radius: 50%; background: var(--white); }
  .church-name { font-weight: 700; }
</style>
</head>
<body>
<main class="poster">
  <div class="scene-photo" role="img" aria-label="Photo of the guest speaker wearing glasses and a headset microphone, in front of a church altar with a crucifix and sunflowers"></div>

  <h2 class="event-title">Rooted Lantern Conference</h2>
  <p class="tagline">Bridging the gap<br>between generations<br>and passing on our<br>deepest beliefs and<br>values.</p>
  <h1 class="speaker-name">Dr. Glen Marlowe</h1>
  <p class="book-title">The Map of Q9</p>

  <div class="book-badge">The Map of Q9</div>

  <p class="event-date">AUGUST 25-26</p>
  <p class="event-times">FRIDAY 8-10 PM &nbsp;|&nbsp; SATURDAY 4-8 PM</p>

  <div class="rule rule-top"></div>
  <div class="cost-tag">
    <svg width="90" height="65" viewBox="0 0 90 65"><polygon points="6,0 78,0 90,32.5 78,65 0,65 8,32.5" fill="#ffffff"/></svg>
    <span>COST</span>
  </div>
  <div class="price price-adult"><div class="price-amount">$15</div><div class="price-label">Adults</div></div>
  <div class="divider divider-a"></div>
  <div class="price price-child"><div class="price-amount">$5</div><div class="price-label">Children</div></div>
  <div class="divider divider-b"></div>
  <p class="cost-note">Covers admission to all sessions and workshops</p>
  <div class="rule rule-bottom"></div>

  <p class="footnote">Refreshments and Saturday dinner. *kids 5 and under free<br>Childcare provided for all sessions.</p>

  <div class="church-line">
    <span class="church-mark"></span>
    <span class="church-name">Cedar Hollow Church</span>
    <span class="church-address">· 4312 Orchard Bend, Missouri City, TX 77512</span>
  </div>
</main>
</body>
</html>
```